property maintenance company covering all trades Plumbing,heating ,electrical building carpentry

business cards

Target Market(s)

DOMESTIC HOUSEHOLDS

Industry/Entity Type

Property Maintenance

Contact Information for Business Card

dorian Fellowes
07841 305918
Brightwell Property Maintenace

Font styles to use
Sans Serif

Colors
eda3c7
d2a4cc
b7a5cd

```html
<!DOCTYPE html>
<html lang="en">
<head>
<meta charset="utf-8">
<title>Brightwell Property Maintenace – Business Card</title>
<link rel="stylesheet" href="https://fonts.googleapis.com/css2?family=Lato:wght@300;400;700&display=swap">
<style>
  :root {
    --pink: #eda3c7;
    --mauve: #d2a4cc;
    --lavender: #b7a5cd;
    --card: #ffffff;
    --backdrop: #ece8ea;
  }
  * { box-sizing: border-box; margin: 0; padding: 0; }
  html, body {
    width: 1200px;
    height: 902px;
    overflow: hidden;
    background: var(--backdrop);
    font-family: "Lato", sans-serif;
  }
  .business-card {
    position: absolute;
    left: 100px;
    top: 166px;
    width: 1000px;
    height: 570px;
    background: var(--card);
    border-radius: 285px 0 0 285px;
    box-shadow: 0 10px 30px rgba(0,0,0,0.12);
  }
  .brand {
    position: absolute;
    left: 60px;
    top: 66px;
    width: 438px;
    height: 438px;
    border-radius: 50%;
    border: 2px solid var(--pink);
    display: flex;
    flex-direction: column;
    align-items: center;
    justify-content: center;
    gap: 18px;
  }
  .brand-dot {
    width: 46px;
    height: 46px;
    border-radius: 50%;
    background: var(--lavender);
  }
  .brand-name {
    color: var(--lavender);
    font-weight: 400;
    font-size: 30px;
    line-height: 1.3;
    letter-spacing: 2px;
    text-align: center;
  }
  .name-band {
    position: absolute;
    left: 545px;
    right: 0;
    top: 82px;
    height: 88px;
    background: var(--pink);
    border-radius: 44px 0 0 44px;
    padding-right: 75px;
    display: flex;
    flex-direction: column;
    justify-content: center;
    align-items: flex-end;
    color: #fff;
  }
  .person-name { font-weight: 700; font-size: 31px; line-height: 1.1; }
  .person-title { font-weight: 300; font-size: 25px; line-height: 1.1; }
  .contact {
    position: absolute;
    left: 559px;
    right: 74px;
    text-align: right;
    color: var(--lavender);
    font-weight: 400;
    font-size: 25px;
    line-height: 35px;
  }
  .contact-address { top: 246px; }
  .contact-lines { top: 350px; }
  .contact-web { top: 450px; }
  .divider {
    position: absolute;
    left: 559px;
    right: 74px;
    height: 2px;
    background: var(--pink);
  }
  .divider-upper { top: 337px; }
  .divider-lower { top: 436px; }
  .label { color: var(--pink); font-weight: 700; }
  .web-domain { color: var(--pink); }
</style>
</head>
<body>
  <main class="business-card">
    <div class="brand">
      <span class="brand-dot"></span>
      <p class="brand-name">Brightwell<br>Property Maintenace</p>
    </div>

    <div class="name-band">
      <p class="person-name">Dorian Fellowes</p>
      <p class="person-title">Chief Executive Officer</p>
    </div>

    <address class="contact contact-address" style="font-style:normal">
      0000 Youe Address,2nd Ste.<br>Ashbury, Texas 1234
    </address>
    <span class="divider divider-upper"></span>

    <p class="contact contact-lines">
      07841 305918 <span class="label">:P</span><br>
      your@companymail.com <span class="label">:E</span>
    </p>
    <span class="divider divider-lower"></span>

    <p class="contact contact-web">www.<span class="web-domain">companyweb</span>.com</p>
  </main>
</body>
</html>
```